Moderne & auffällige Fahrzeugbeschriftung für Handwerksunternehmen
Zielgruppe
Wir sind ein Handwerksunternehmen fürGebäudereinigung und auch Immobilieservice mit Sitz in Berlin. Wir arbeiten für Hausverwaltungen, Baufirmen, und Architekten. Wir führen auch Sonderreinigung wie Grundreinigungen etc. aus.
Aufgabenstellung
Wir suchen ein modernes und Auffälliges Design ( gerne auch Teilfolierung )für unseren Fuhrpark. Farbgebung sollte sich am Logo orientieren und grün/grau/anthrazit sein. Wir setzen vor folgenden Fahrzeuge ein:
Velmora Korvat, Velmora Tundex, Velmora Pilsu sowie Velmora Astrinn ( PKW keine Schiebetüren ) ein.
Alle besitzen seitlich eine Schiebetür. Alle unsere Autos sind weiß lackiert. Dementsprechend können Farben ruhig etwas großzügiger eingesetzt werden. Das Design soll am Ende ohne Probleme auch an andere Marken Anwendung finden können

```html
<!DOCTYPE html>
<html lang="de">
<head>
<meta charset="utf-8">
<title>Halbern Dienstleistungen – Fahrzeugbeschriftung</title>
<link rel="stylesheet" href="https://fonts.googleapis.com/css2?family=Libre+Baskerville&display=swap">
<style>
  :root {
    --bg: #efefef;
    --panel: #ffffff;
    --green: #1f9e48;
    --green-deep: #0a7a30;
    --anthracite: #4a4a4c;
  }
  html, body {
    margin: 0;
    width: 1200px;
    height: 794px;
    overflow: hidden;
    background: var(--bg);
  }
  .canvas {
    position: relative;
    width: 1200px;
    height: 794px;
  }
  .wrap-graphic {
    position: absolute;
    left: 0;
    top: 0;
  }
  .web-address {
    position: absolute;
    right: 170px;
    top: 240px;
    margin: 0;
    font-family: "Libre Baskerville", Georgia, serif;
    font-size: 17px;
    color: var(--anthracite);
  }
  .brand {
    position: absolute;
    left: 520px;
    top: 348px;
    display: flex;
    align-items: flex-start;
    gap: 18px;
  }
  .brand-square {
    width: 26px;
    height: 26px;
    margin-top: 10px;
    background: var(--green);
  }
  .brand-name {
    margin: 0;
    font-family: "Libre Baskerville", Georgia, serif;
    font-weight: 400;
    font-size: 34px;
    line-height: 1.3;
    color: var(--anthracite);
  }
</style>
</head>
<body>
<div class="canvas">
  <svg class="wrap-graphic" width="1200" height="794" viewBox="0 0 1200 794" aria-hidden="true">
    <defs>
      <clipPath id="panel-shape">
        <rect x="128" y="222" width="946" height="370" rx="26"/>
      </clipPath>
    </defs>
    <rect class="side-panel" x="128" y="222" width="946" height="370" rx="26" fill="var(--panel)"/>
    <g clip-path="url(#panel-shape)">
      <polygon class="accent-stripe" points="128,506 1074,452 1074,460 128,514" fill="var(--anthracite)"/>
      <polygon class="lower-band" points="128,524 1074,472 1074,592 128,592" fill="var(--green)"/>
      <rect class="base-strip" x="128" y="566" width="946" height="26" fill="var(--green-deep)"/>
    </g>
  </svg>

  <p class="web-address">www.berlin-hausservice-beispiel.de</p>

  <div class="brand">
    <span class="brand-square"></span>
    <p class="brand-name">Halbern<br>Dienstleistungen GmbH</p>
  </div>
</div>
</body>
</html>
```